Zielgruppe
Die Kessler-Volkshochschule Kreis Aurental ist eine gemeinnützige Einrichtung zur Erwachsenen- und Weiterbildung mit ca. 5.000 Veranstaltungen pro Jahr.
Volkshochschulen sind entgegen ihrer Bezeichnung keine Hochschulen oder Schulen, sondern in Deutschland dem Bildungsbereich der Weiterbildung zugeordnet.
Aufgabenstellung
Die Kessler-Volkshochschule Kreis Aurental möchte mit einer neuen Webseite, welche auch für mobile Geräte geeignet sein muss, Ihren neuen Internetauftritt umsetzen.
Vorgaben:
- der Internetauftritt soll modern gestaltet sein.
- die unter Dateien befindlichen Guidelines müssen eingehalten werden. Wichtig hierbei ist, dass die 6 Symbole auf die Startseite für die Auswahl der jeweiligen Kursbereiche integriert werden. Hierbei ist zu beachten, dass die Anzahl der Symbole erweiterbar ist.
Als CMS wird Typo3 genutzt.
Es geht um die Erstellung der Startseite auf welcher auch News untergebracht werden sollen - ggf. in Kachelform. Und die Erstellung einer Unterseite.

```html
<!DOCTYPE html>
<html lang="de">
<head>
<meta charset="utf-8">
<title>Kessler-Volkshochschule Kreis Aurental</title>
<link href="https://fonts.googleapis.com/css2?family=Roboto+Condensed:wght@300;400;700&display=swap" rel="stylesheet">
<style>
:root{
  --navy:#0d2e5c;
  --blue:#1f4e8c;
  --green:#a9c91f;
  --text:#8a8a8a;
  --title:#2b5d9b;
  --line:#d8d8d8;
  --bg:#ffffff;
}
*{margin:0;padding:0;box-sizing:border-box}
html,body{width:813px;height:1200px;overflow:hidden;background:var(--bg)}
body{position:relative;font-family:"Roboto Condensed",Arial,sans-serif;font-weight:300;color:var(--text)}
.abs{position:absolute}
.brand{left:206px;top:10px;display:flex;align-items:center;gap:6px}
.brand-dot{width:12px;height:12px;border-radius:50%;background:var(--blue)}
.brand-name{font-size:7px;line-height:8px;color:var(--navy);font-weight:400}
.district{left:362px;top:14px;display:flex;align-items:center;gap:4px;font-size:4.5px;color:#aaa;line-height:5px;letter-spacing:.3px}
.district .ring{width:13px;height:13px;border:1px solid #bbb;border-radius:50%}
.field{top:11px;width:63px;height:14px;border:1px solid #e0e0e0;font-size:5.5px;font-style:italic;color:#c5c5c5;padding:4px 4px}
.login{left:580px;top:11px;width:31px;height:14px;background:var(--navy);color:#fff;font-size:5.5px;font-weight:400;text-align:center;line-height:14px}
.nav{left:201px;top:38px;width:411px;height:17px;border-top:1px solid #ccc;border-bottom:1px solid #ccc;display:flex;justify-content:space-between;align-items:center;padding:0 15px 0 4px}
.nav span{font-size:6px;color:#999}
.nav .active{color:var(--navy);border-top:1px solid var(--navy);margin-top:-2px;padding:5px 9px 0}
.hero{left:201px;top:62.5px;width:411px;height:188px;background:linear-gradient(120deg,#e9eef2 0%,#b9c7d2 45%,#7d8e9f 70%,#c7b9a3 100%)}
.hero-circle{left:213px;top:76px;width:160px;height:160px;border-radius:50%;background:var(--green);color:#fff;padding:38px 10px 0 19px}
.hero-circle h1{font-weight:300;font-size:16px;line-height:17px}
.hero-circle h2{font-weight:300;font-size:9.5px;line-height:12px;margin-bottom:6px}
.hero-circle p{font-size:5.6px;line-height:8.2px}
.more-btn{left:332px;top:204.5px;width:27px;height:27px;border-radius:50%;background:#5fae2e;color:#fff;font-size:6.5px;text-align:center;line-height:27px}
.dots{left:580px;top:242px;display:flex;gap:2px}
.dots i{width:4px;height:4px;border-radius:50%;background:#fff;opacity:.7;display:block}
.dots i:first-child{background:var(--blue);opacity:1}
.section-title{left:0;width:813px;top:266px;text-align:center;font-size:12.5px;color:var(--navy)}
.cat{top:300px;width:60px;text-align:center;font-size:6px;color:#999}
.cat .circle{width:46px;height:46px;border-radius:50%;margin:0 auto 9px;border:2px solid #f0f0f0}
.heading{left:201px;width:302px;display:flex;align-items:center;gap:4px;font-size:8.5px;color:var(--navy);font-weight:400}
.heading::before{content:"";width:4px;height:2px;background:var(--navy)}
.heading::after{content:"";flex:1;height:2px;background:var(--navy)}
.card{top:401px;width:96.5px;height:111px;border-bottom:1px solid}
.card .pic{height:65.5px}
.card h3{font-weight:300;font-size:7px;color:var(--title);margin:4px 4px 3px}
.card p{font-size:4.8px;line-height:7.2px;margin:0 4px}
.promo{left:516px;top:386px;width:96px;height:123px;background:linear-gradient(#f0f6dc,#cfe29a);padding:8px 7px}
.promo small{font-size:7.5px;color:#999;display:block}
.promo strong{font-size:9.5px;color:var(--navy);font-weight:700}
.badge{left:578px;top:404px;width:30px;height:30px;border-radius:50%;background:#e3161c;color:#fff;font-weight:700;font-size:9px;text-align:center;line-height:30px}
.pdf{left:516px;top:518px;width:96px;height:122px;background:#e9ebee;padding:8px 11px}
.pdf small{font-size:7.5px;color:#999;display:block}
.pdf strong{font-size:8px;color:var(--navy);font-weight:700}
.booklet{left:526px;top:552px;width:48px;height:80px;background:linear-gradient(135deg,#fff,#d6dfea)}
.dl{left:565px;top:592.5px;width:40px;height:40px;border-radius:50%;background:var(--navy);color:#fff;font-size:6px;text-align:center;line-height:40px}
.post-pic{left:200px;width:132px;height:98px}
.post{left:343px;width:161px}
.post h3{font-weight:300;font-size:8px;line-height:10px;color:var(--title);text-transform:uppercase;margin-bottom:9px}
.post p{font-size:5px;line-height:7.1px;padding-left:1px}
.mehr{left:345px;display:flex;align-items:center;gap:3px;font-size:5px;color:var(--navy);font-weight:400}
.mehr svg{width:8px;height:8px}
.sep{left:200px;width:304px;height:1px;background:var(--line)}
.partners{left:206px;top:1058px;width:400px;display:flex;justify-content:space-between;align-items:center}
.partners span{font-size:7px;font-weight:700;color:var(--navy)}
.foot-line{left:200px;top:1128px;width:412px;height:2px;background:var(--navy)}
.foot{top:1146px;font-size:5px;line-height:7.2px;color:#999;text-transform:uppercase}
.foot.addr{text-transform:none}
</style>
</head>
<body>

<div class="abs brand"><span class="brand-dot"></span><span class="brand-name">Kessler-Volkshochschule<br>Landkreis Aurental</span></div>
<div class="abs district"><span class="ring"></span><span>LANDKREIS<br>AURENTAL</span></div>
<div class="abs field" style="left:443px">Username:</div>
<div class="abs field" style="left:512px">Password</div>
<div class="abs login">LOGIN</div>

<nav class="abs nav">
  <span class="active">STARTSEITE</span><span>ÖFFNUNGSZEITEN</span><span>FÖRDERUNGEN</span><span>SERVICE</span><span>ÜBER UNS</span><span>UNSERE DOZENTEN</span><span>KONTAKT</span>
</nav>

<div class="abs hero" role="img" aria-label="Foto: junge Erwachsene lernen gemeinsam am Laptop"></div>
<div class="abs hero-circle">
  <h1>Wellcome to</h1>
  <h2>Volkshochschule Aurental</h2>
  <p>Lorem Ipsum is simply dummy text of the printing and typesetting industry. Lorem Ipsum has been the industry's standard dummy text ever since the 1500s, when an unknown printer took a galley of type and scrambled it to make a type specimen book</p>
</div>
<div class="abs more-btn">MEHR</div>
<div class="abs dots"><i></i><i></i><i></i><i></i></div>

<div class="abs section-title">Our Kursprogramm</div>
<div class="abs cat" style="left:199px"><div class="circle" style="background:#55b6e6"></div>Beruf</div>
<div class="abs cat" style="left:270px"><div class="circle" style="background:#7b57a6"></div>Sprachen</div>
<div class="abs cat" style="left:340px"><div class="circle" style="background:#93c020"></div>Gesundheit</div>
<div class="abs cat" style="left:411px"><div class="circle" style="background:#e3161c"></div>Kultur</div>
<div class="abs cat" style="left:482px"><div class="circle" style="background:#ef6b10"></div>Gesellshaft</div>
<div class="abs cat" style="left:553px"><div class="circle" style="background:#f7b500"></div>Grundbildung</div>

<div class="abs heading" style="top:382px">LAST NEWS</div>
<div class="abs card" style="left:201px;border-color:var(--green)">
  <div class="pic" role="img" aria-label="Foto: Naturheilmittel mit Blüten" style="background:linear-gradient(#f3e9b0,#9cae4c)"></div>
  <h3>Fit in den Winter</h3>
  <p>Eine starke Abwehrkraft ist wichtig für die kalte Jahreszeit. Wir sprechen über Heilmittel aus der Naturheilkunde,</p>
</div>
<div class="abs card" style="left:303.5px;border-color:#5aa0d8">
  <div class="pic" role="img" aria-label="Grafik: Kursbild Grafik-Suite 6" style="background:linear-gradient(135deg,#5a1020,#c2282a,#2b1a3a)"></div>
  <h3>Grafik-Suite 6 für vhs</h3>
  <p>Eine starke Abwehrkraft ist wichtig für die kalte Jahreszeit. Wir sprechen über Heilmittel aus der Naturheilkunde,</p>
</div>
<div class="abs card" style="left:406px;border-color:#ef6b10">
  <div class="pic" role="img" aria-label="Foto: Berglandschaft mit Savanne" style="background:linear-gradient(#a9bcd0,#6b6f60 60%,#5a3e2a)"></div>
  <h3>Grafik-Suite 6 für vhs</h3>
  <p>Eine starke Abwehrkraft ist wichtig für die kalte Jahreszeit. Wir sprechen über Heilmittel aus der Naturheilkunde,</p>
</div>

<div class="abs promo" role="img" aria-label="Aktion Gesundheit: Person beim Yoga"><small>Kursprogramm Aktion</small><strong>GESUNDHEIT</strong></div>
<div class="abs badge">-70%</div>
<div class="abs pdf"><small>PDF Download</small><strong>PROGRAMMHEFT</strong></div>
<div class="abs booklet" role="img" aria-label="Titelseite des Programmhefts"></div>
<div class="abs dl">DOWNLOAD</div>

<div class="abs heading" style="top:529px">LAST POSTS</div>

<div class="abs post-pic" style="top:553px;background:linear-gradient(#d9dde2,#7e7466)" role="img" aria-label="Foto: Besuchergruppe bei einem Ortsrundgang"></div>
<div class="abs post" style="top:555px">
  <h3>Politik.live - Ortskernsanierung<br>in Erlenhausen</h3>
  <p>Rund 15 interessierte Bürgerinnen und Bürger konnte VHS-Leiter Jörg Brandauer bei der Veranstaltung Politik.Live - Ortskernsanierung in Erlenhausen - gestern und heute in Erlenhausen begrüßen. Bürgermeisterin Britta Lohmeyer führte mit viel Elan durch den Ortskern von Erlenhausen und zeigte auf, welchen Flecken in die Ortskernsanierung III aufgenommen werden sollen und welche Maßnahmen bereits seit 1977 mit den Sanierungsmaßnahmen I und II umgesetzt wurden.</p>
</div>
<div class="abs mehr" style="top:641px"><svg viewBox="0 0 8 8"><circle cx="4" cy="4" r="4" fill="#0d2e5c"/><path d="M2.3 4h3.2M4.2 2.7 5.5 4 4.2 5.3" stroke="#fff" stroke-width=".7" fill="none"/></svg>MEHR</div>
<div class="abs sep" style="top:666px"></div>

<div class="abs post-pic" style="top:678px;background:linear-gradient(#e3e6e8,#8f9a7e 55%,#6e7a52)" role="img" aria-label="Foto: Rundgang am Schulcampus"></div>
<div class="abs post" style="top:681px">
  <h3>„Politik live“ in Sachtal</h3>
  <p>Bei einem Rundgang mit Herrn Bürgermeister Wendling wurde den Teilnehmern vorgestellt, was die Stadt Sachtal unter Familien- und Bürgerfreundlichkeit versteht und welche konkreten Verbesserungen bereits eingeleitet sind. Nach einer kurzen Begrüßung beim Kulturhaus ging es weiter über den Schulcampus. Neben Informationen zu den anliegenden Schulen und deren künftiger Entwicklung gab es immer wieder Fakten zum Themenbereich Energie und Heizen.</p>
</div>
<div class="abs mehr" style="top:759px"><svg viewBox="0 0 8 8"><circle cx="4" cy="4" r="4" fill="#0d2e5c"/><path d="M2.3 4h3.2M4.2 2.7 5.5 4 4.2 5.3" stroke="#fff" stroke-width=".7" fill="none"/></svg>MEHR</div>
<div class="abs sep" style="top:791px"></div>

<div class="abs post-pic" style="top:803px;background:linear-gradient(#c9cdd2,#8a8e94 60%,#3a3d42)" role="img" aria-label="Foto: Gruppe vor einem silbernen Sportwagen"></div>
<div class="abs post" style="top:806px">
  <h3>Führung bei<br>Velora: V8 Sportwagenmanufaktur</h3>
  <p>Nach einem kurzen Einblick in die Firmengeschichte bzw. wie es zu dem Namen Velora AG gekommen ist, wurde die Gruppe mit dem Bus über das Firmengelände zur Sportwagen Manufaktur gebracht. Die Führung war sehr interessant und kurzweilig. Von Station zu Station konnte die Entstehung des Velora V8 verfolgt werden, der noch zu 75% per Hand entsteht, daher auch der Name "Manufaktur". Jeder V8 ein Unikat, jeder Kundenwunsch wird erfüllt.</p>
</div>
<div class="abs mehr" style="top:890.5px"><svg viewBox="0 0 8 8"><circle cx="4" cy="4" r="4" fill="#0d2e5c"/><path d="M2.3 4h3.2M4.2 2.7 5.5 4 4.2 5.3" stroke="#fff" stroke-width=".7" fill="none"/></svg>MEHR</div>
<div class="abs sep" style="top:916px"></div>

<div class="abs post-pic" style="top:925.5px;background:linear-gradient(#2f6fc4,#9cc2e8 30%,#3f8a2c 55%,#62b02e)" role="img" aria-label="Foto: grüne Hügellandschaft unter blauem Himmel"></div>
<div class="abs post" style="top:928px">
  <h3>Vortrag Nord-Ost-Indien -<br>Naturparadiese, Völkermosaik und Himalaya</h3>
  <p>Die Reise beginnt im Kaziranga N.P. in Assam. Hier haben die Indischen Panzernashörner einen ihrer letzten Lebensräume. Von hier geht es weiter nach Shillong im Bundesstaat Meghalaya. Nächste Station ist Darjeeling, mit atemberaubenden Ausblicken auf den Himalaya. Das letzte Ziel ist der Bundesstaat Sikkim, mit der Hauptstadt Gantok, bis 1975 ein eigenständiges Königreich.</p>
</div>
<div class="abs mehr" style="top:1013px"><svg viewBox="0 0 8 8"><circle cx="4" cy="4" r="4" fill="#0d2e5c"/><path d="M2.3 4h3.2M4.2 2.7 5.5 4 4.2 5.3" stroke="#fff" stroke-width=".7" fill="none"/></svg>MEHR</div>
<div class="abs sep" style="top:1039px"></div>

<div class="abs partners">
  <span>Lernwerkstatt</span><span>Die Lernprämie</span><span>Junge VHS Aurental</span><span>Sprachschule Aurental</span><span>Kurs-Gutscheine</span>
</div>

<div class="abs foot-line"></div>
<div class="abs foot" style="left:207px">Startseite<br>Kursprogramm<br>Last-Minute-Kurse<br>Dozenten-Login<br>Teilnehmerinfos<br>Kursberatung<br>Ansprechpartner/innen</div>
<div class="abs foot" style="left:310px;top:1147px">Geschäftsstellen<br>Wir über uns<br>Dozenteninfos<br>AGB<br>Widerrufsrecht<br>Impressum</div>
<div class="abs foot" style="left:413px">Sprachen<br>VHS Kulturzone<br>Easy-Uni<br>Firmenservice<br>Projekte<br>Abitur am Abend</div>
<div class="abs foot addr" style="left:504px">Kreis Aurental<br>Lindenallee 12<br>74999 Aurental<br>E-Mail: info@kessler-vhs.example<br>Telefon: 07000 555-1010<br>Telefax: 07000 555-1011</div>

</body>
</html>
```